Boutique custom software development company needs new business card

Our nearly 20 year old custom software development company would like to better include the fact that we are now providing Bitcoin services. These new services are B2B include education (how to acquire and securely hold Bitcoin) and integrating Bitcoin payments into existing ecommerce sites or other existing systems. Please keep the card clean and simple. Attached is our current design and some other files. vexalon.example

Target Market(s)

businesses owners interested in long term relationship

Industry/Entity Type

Custom software development and Bitcoin

Contact Information for Business Card

Marcus Ellwood, marcus@vexalon.example, vexalon.example, (888) 555-VEXAL

Font styles to use
Other font styles liked:
• monospace

Requirements
Must have
• double-sided
Nice to have
• clean and simple
Should not have
• physical address

```html
<!DOCTYPE html>
<html lang="en">
<head>
<meta charset="utf-8">
<title>Vexalon Business Card</title>
<link rel="stylesheet" href="https://fonts.googleapis.com/css2?family=Roboto+Mono:wght@400;700&family=Lato:wght@300&display=swap">
<style>
  :root {
    --backdrop: #e6e4e0;
    --card-navy: #13184a;
    --emboss-navy: #1d2160;
    --tagline-navy: #232765;
    --accent-orange: #f07f23;
    --brand-blue: #3f76ba;
    --text-white: #ffffff;
  }
  * { margin: 0; padding: 0; box-sizing: border-box; }
  html, body {
    width: 900px;
    height: 1200px;
    overflow: hidden;
    background: var(--backdrop);
  }
  .canvas {
    position: relative;
    width: 900px;
    height: 1200px;
  }
  .card {
    position: absolute;
    left: 78px;
    width: 744px;
    height: 442px;
    border-radius: 30px;
    background: var(--card-navy);
    overflow: hidden;
  }
  .card--front { top: 130px; }
  .card--back { top: 638px; }

  .brand-block {
    position: absolute;
    left: 67px;
    top: 79px;
    width: 276px;
    height: 286px;
    display: flex;
    align-items: center;
    gap: 16px;
  }
  .brand-square {
    width: 44px;
    height: 44px;
    background: var(--brand-blue);
    flex-shrink: 0;
  }
  .brand-name {
    font-family: "Roboto Mono", monospace;
    font-weight: 700;
    font-size: 34px;
    color: var(--text-white);
    letter-spacing: 1px;
  }
  .divider {
    position: absolute;
    left: 376px;
    top: 79px;
    width: 2px;
    height: 286px;
    background: var(--accent-orange);
  }
  .details {
    position: absolute;
    left: 407px;
    top: 98px;
    width: 310px;
    font-family: "Roboto Mono", monospace;
    color: var(--text-white);
  }
  .person-name {
    font-weight: 700;
    font-size: 28px;
    line-height: 36px;
    color: var(--accent-orange);
  }
  .person-title {
    font-size: 15px;
    line-height: 24px;
    letter-spacing: 0.5px;
  }
  .contact-list {
    list-style: none;
    margin-top: 28px;
  }
  .contact-item {
    display: flex;
    align-items: center;
    gap: 8px;
    font-size: 15px;
    line-height: 25.5px;
  }
  .contact-icon { width: 17px; height: 17px; fill: var(--accent-orange); }
  .services {
    margin-top: 32px;
    font-size: 15.5px;
    line-height: 25px;
    letter-spacing: 0.3px;
  }

  .back-name {
    position: absolute;
    left: 0;
    right: 0;
    top: 92px;
    text-align: center;
    font-family: "Roboto Mono", monospace;
    font-weight: 700;
    font-size: 150px;
    line-height: 170px;
    color: var(--emboss-navy);
  }
  .back-tagline {
    position: absolute;
    left: 0;
    right: 0;
    top: 268px;
    text-align: center;
    font-family: "Lato", sans-serif;
    font-weight: 300;
    font-size: 42px;
    letter-spacing: -1px;
    color: var(--tagline-navy);
    white-space: nowrap;
  }
</style>
</head>
<body>
<main class="canvas">
  <section class="card card--front">
    <div class="brand-block">
      <span class="brand-square"></span>
      <span class="brand-name">VEXALON</span>
    </div>
    <div class="divider"></div>
    <div class="details">
      <h1 class="person-name">Marcus Ellwood</h1>
      <p class="person-title">Founding Partner</p>
      <ul class="contact-list">
        <li class="contact-item">
          <svg class="contact-icon" viewBox="0 0 16 16" aria-hidden="true"><path d="M1 6c0-2 3-4 7-4s7 2 7 4v1h-4V5.5H5V7H1z"/><path d="M3 8h10l1 6H2z"/><circle cx="8" cy="11" r="1.6" fill="#13184a"/></svg>
          <span>(888) 555-VEXAL</span>
        </li>
        <li class="contact-item">
          <svg class="contact-icon" viewBox="0 0 16 16" aria-hidden="true"><path d="M1 3h14v1.5L8 9 1 4.5z"/><path d="M1 6l7 4.5L15 6v7H1z"/></svg>
          <span>marcus@vexalon.example</span>
        </li>
        <li class="contact-item">
          <svg class="contact-icon" viewBox="0 0 16 16" aria-hidden="true"><circle cx="8" cy="8" r="7"/><path d="M4 4c2 0 3 1 2 3s-3 1-3 3M10 2.5c-1 2 1 3 3 3M9 14c0-2 2-3 3-5" stroke="#13184a" stroke-width="1.2" fill="none"/></svg>
          <span>vexalon.example</span>
        </li>
      </ul>
      <p class="services">Custom Software &amp;<br>Bitcoin Services</p>
    </div>
  </section>

  <section class="card card--back">
    <p class="back-name">VEXALON</p>
    <p class="back-tagline">custom software &amp; bitcoin services</p>
  </section>
</main>
</body>
</html>
```